HRWC Foldable Flyer

Design a flyer, foldable. To fit in an envelope and/or drop off at doctor office for an outpatient physical therapy clinic, Harborridgewellness.com.
Emphasis on appointments two weeks out, taking new patients, and use website for photos

```html
<!DOCTYPE html>
<html lang="en">
<head>
<meta charset="utf-8">
<title>HRWC Flyer</title>
<link href="https://fonts.googleapis.com/css2?family=Poppins:wght@300;400;500;600;700;800&display=swap" rel="stylesheet">
<style>
  :root {
    --navy: #1b5e86;
    --steel: #86a9bb;
    --slate: #8e939b;
    --ink: #1f2a33;
    --white: #ffffff;
    --photo-a: #c4c6c2;
    --photo-b: #a4a8a5;
    --photo-c: #7b7a8a;
  }
  * { box-sizing: border-box; margin: 0; padding: 0; }
  html, body { width: 846px; height: 1200px; overflow: hidden; background: var(--white); }
  .flyer {
    position: relative; width: 846px; height: 1200px; overflow: hidden;
    font-family: "Poppins", sans-serif; color: var(--ink); background: var(--white);
  }
  .top-band { position: absolute; left: 0; top: 0; width: 846px; height: 401px; background: var(--navy); }
  .side-band { position: absolute; left: 322px; top: 353px; width: 524px; height: 540px; background: var(--navy); }

  .brand {
    position: absolute; left: 54px; top: 73px; width: 200px; height: 200px;
    display: flex; flex-direction: column; align-items: center; justify-content: center; gap: 10px;
  }
  .brand-dot { width: 14px; height: 14px; border-radius: 50%; background: var(--white); }
  .brand-name { font-weight: 700; font-size: 44px; color: var(--white); letter-spacing: 2px; line-height: 1; }

  .headline {
    position: absolute; left: 307px; top: 46px; width: 520px;
    color: var(--white); font-size: 43px; line-height: 53px; font-weight: 300; text-transform: uppercase;
  }
  .headline strong { font-weight: 700; }
  .tagline { position: absolute; left: 307px; top: 272px; color: var(--white); font-weight: 500; font-size: 22px; }

  .services-pill {
    position: absolute; left: 55px; top: 363px; width: 520px; height: 78px;
    background: var(--steel); border-radius: 39px 0 0 39px;
    padding-left: 51px; display: flex; align-items: center;
    color: var(--white); font-size: 35px; font-weight: 300;
  }
  .services-pill strong { font-weight: 700; margin-left: 10px; }

  .photo {
    position: absolute; left: 322px; top: 353px; width: 524px; height: 524px;
    border-radius: 262px 262px 0 0;
    background: linear-gradient(100deg, var(--photo-a) 0%, var(--photo-b) 55%, var(--photo-c) 100%);
  }

  .intro { position: absolute; left: 54px; top: 467px; width: 265px; font-size: 14.5px; line-height: 24.2px; }

  .service-list { position: absolute; left: 54px; top: 612px; width: 240px; list-style: none; }
  .service-list li {
    position: relative; padding-left: 30px; font-weight: 700; font-size: 17px; line-height: 23.5px; margin-bottom: 12px;
  }
  .service-list li svg { position: absolute; left: 1px; top: 4px; width: 15px; height: 15px; }
  .service-list li.tall { margin-bottom: 14px; }

  .backdrop { position: absolute; left: 0; top: 938px; width: 846px; height: 262px; }

  .book-pill {
    position: absolute; left: 255px; top: 877px; width: 591px; height: 61px;
    background: var(--navy); border-radius: 31px 0 0 31px;
    display: flex; align-items: center; justify-content: flex-end; padding-right: 55px;
    color: var(--white); font-size: 25.5px; font-weight: 300;
  }
  .book-pill strong { font-weight: 700; margin-left: 8px; }

  .contact { position: absolute; right: 55px; top: 966px; text-align: right; color: var(--white); }
  .contact .label { font-size: 25px; font-weight: 300; line-height: 1.3; }
  .contact .value { font-size: 24px; font-weight: 700; line-height: 31px; margin-top: 8px; margin-bottom: 22px; }
  .contact .url { font-size: 26px; font-weight: 700; margin-top: 12px; }
</style>
</head>
<body>
<div class="flyer">
  <div class="top-band"></div>
  <div class="side-band"></div>

  <div class="brand">
    <span class="brand-dot"></span>
    <span class="brand-name">HRWC</span>
  </div>

  <h1 class="headline">Open doors, open schedule — <strong>new patients seen within 14 days.</strong></h1>
  <p class="tagline">Helping You Move Better And Feel Better</p>

  <div class="photo" role="img" aria-label="Photo of hands holding an anatomical pelvis model"></div>

  <div class="services-pill">OUR <strong>SERVICES</strong></div>

  <p class="intro">At HRWC, we provided an in depth evaluation in order to determine what is the best way to get you out of pain, back to work or doing the things you want to do.</p>

  <ul class="service-list">
    <li><svg viewBox="0 0 16 16"><circle cx="8" cy="8" r="8" fill="#1b5e86"/><path d="M4.5 8.2l2.3 2.3 4.7-4.8" fill="none" stroke="#fff" stroke-width="2" stroke-linecap="round" stroke-linejoin="round"/></svg>Manual Therapy</li>
    <li class="tall"><svg viewBox="0 0 16 16"><circle cx="8" cy="8" r="8" fill="#1b5e86"/><path d="M4.5 8.2l2.3 2.3 4.7-4.8" fill="none" stroke="#fff" stroke-width="2" stroke-linecap="round" stroke-linejoin="round"/></svg>Myofascial Decompression</li>
    <li><svg viewBox="0 0 16 16"><circle cx="8" cy="8" r="8" fill="#1b5e86"/><path d="M4.5 8.2l2.3 2.3 4.7-4.8" fill="none" stroke="#fff" stroke-width="2" stroke-linecap="round" stroke-linejoin="round"/></svg>IASTM</li>
    <li class="tall"><svg viewBox="0 0 16 16"><circle cx="8" cy="8" r="8" fill="#1b5e86"/><path d="M4.5 8.2l2.3 2.3 4.7-4.8" fill="none" stroke="#fff" stroke-width="2" stroke-linecap="round" stroke-linejoin="round"/></svg>Evidence Based Exercise</li>
    <li class="tall"><svg viewBox="0 0 16 16"><circle cx="8" cy="8" r="8" fill="#1b5e86"/><path d="M4.5 8.2l2.3 2.3 4.7-4.8" fill="none" stroke="#fff" stroke-width="2" stroke-linecap="round" stroke-linejoin="round"/></svg>Pelvic Floor Therapy &amp; Women's Health</li>
    <li><svg viewBox="0 0 16 16"><circle cx="8" cy="8" r="8" fill="#1b5e86"/><path d="M4.5 8.2l2.3 2.3 4.7-4.8" fill="none" stroke="#fff" stroke-width="2" stroke-linecap="round" stroke-linejoin="round"/></svg>SwallowFlex Speech Therapy</li>
  </ul>

  <svg class="backdrop" viewBox="0 0 846 262" preserveAspectRatio="none">
    <path d="M0 92 C120 92 220 60 275 0 L846 0 L846 262 L0 262 Z" fill="#8e939b"/>
  </svg>

  <div class="book-pill">Book An Appointment:<strong>555-218-4470</strong></div>

  <div class="contact">
    <p class="label">Address:</p>
    <p class="value">742 Harbor Ridge Rd, Suite B Alder Bay,<br>CA 90417</p>
    <p class="label">Website:</p>
    <p class="url">www.harborridgewellness.com/</p>
  </div>
</div>
</body>
</html>
```